Infographic to communicate Cyber Security and Insurance Product Offering for IT Service Providers

We need an inspirational infographic that shows how TrellaWorks works with QDR (an MSP partner) to help organisations close the loop on cyber risk. The design should illustrate the layers of the IT infrastructure stack and the systems and processes that wrap around it to protect and mitigate against risk.
At the core: MSP Services (Desktop, Software, Website). Surrounding this: TrellaWorks Governance & Protection, leading into an Incident layer that connects to TrellaWorks Insurance and Incident Response, linked by a continuous feedback loop. The outer circle should represent the constant threat of cyber attack.
TrellaWorks core offerings for this graphic:
Plinth Verify (compliance/assurance product)
Plinth Cover
QDR Primary Services (directly connected to TrellaWorks):
Managed IT Services
Disaster Recovery as a Service (DRaaS)
E8 Security Packages
Cloud Hosting & Infrastructure
QDR Secondary Services (supporting but not directly anchored):
Telephony & Unified Communications
Networking Services
Data Backup & Storage Solutions
Professional Services & Consulting
Procurement & Licensing
Training & User Awareness
Style: Modern, professional, and client-friendly, with a technology-inspired colour palette.
Deliverables: Polished colour version plus editable source files — preferably in Figma, or alternatively if not possible using either Adobe Illustrator (.AI) or a layered Photoshop (.PSD) (e.g. industry standards for editable design).
Rewards: The winning design prize will be increased by $100, and we will also award $50 each to the 2nd and 3rd place runner-ups, as our way of giving a little more back.
A simple wireframe visual guide has been uploaded as a reference, but this should in no way limit or restrict your creativity. We encourage original, innovative approaches to bring this concept to life.
Ownership & Exclusivity: As per ArtMarquee’s T&Cs, all rights to the winning design will transfer to us once the project is complete for our ongoing use. We also kindly ask that the work created here remain exclusive to this project, meaning it won’t be reused or lightly modified for other clients in the future. The reason is simple: once we’ve invested in and paid for a design, we want to be confident it won’t turn up on a competitor’s website with just a different colour scheme. Thanks again for respecting that. [Note:- The designs submitted so far haven’t quite hit the mark, so I’ve put together a couple of slides to clarify direction. These outline the key stakeholders, the current IT services and challenges, how the Morvane product addresses those challenges, and a simple version of what we’d like the infographic to convey. Please review these slides carefully, as they should give you a clearer understanding of the story we want the design to tell.]
Target Market(s)
Small to Medium sized businesses
Colors
Designer to choose colors to be used in the design.
Look and feel

```html
<!DOCTYPE html>
<html lang="en">
<head>
<meta charset="utf-8">
<title>QDR MSP Services – TrellaWorks Cyber Risk Loop</title>
<link href="https://fonts.googleapis.com/css2?family=Montserrat:wght@300;700&display=swap" rel="stylesheet">
<style>
  :root {
    --navy: #1e3a55;
    --crimson: #961215;
    --mist: #c5d1db;
    --frost: #e4e8ed;
    --white: #ffffff;
    --frame: #5a5a5a;
  }
  html, body {
    margin: 0;
    padding: 0;
    width: 1200px;
    height: 1200px;
    overflow: hidden;
    background: var(--white);
  }
  .canvas {
    width: 1200px;
    height: 1200px;
    box-sizing: border-box;
    border: 1px solid var(--frame);
    background: var(--white);
  }
  .risk-diagram { display: block; width: 100%; height: 100%; }
  .risk-diagram text {
    font-family: "Montserrat", sans-serif;
    font-weight: 700;
  }
  .ring-threat { fill: var(--navy); }
  .ring-incident { fill: var(--crimson); }
  .ring-trellaworks { fill: var(--mist); }
  .ring-divider { fill: var(--frost); }
  .core-disc { fill: var(--frost); }
  .service-arrow { fill: var(--navy); }
  .feedback-arrow { fill: var(--navy); }
  .label-outer { fill: var(--white); font-size: 56px; letter-spacing: 4px; }
  .label-incident { fill: var(--white); font-size: 50px; letter-spacing: 4px; }
  .label-layer { fill: var(--navy); font-size: 58px; letter-spacing: 5px; }
  .label-service { fill: var(--white); font-size: 56px; letter-spacing: 4px; }
  .label-feedback {
    fill: var(--white);
    font-size: 30px;
    letter-spacing: 2px;
    font-weight: 300 !important;
  }
  .label-core { fill: var(--navy); font-size: 102px; letter-spacing: 2px; }
</style>
</head>
<body>
<div class="canvas">
  <svg class="risk-diagram" viewBox="0 0 1932 1932" xmlns="http://www.w3.org/2000/svg" role="img" aria-label="QDR MSP services wrapped by TrellaWorks governance, protection, incident, insurance and incident response layers">
    <defs>
      <path id="arc-insurance" d="M 274 966 A 692 692 0 0 1 1658 966"/>
      <path id="arc-response" d="M 232 966 A 734 734 0 0 0 1700 966"/>
      <path id="arc-incident" d="M 321 966 A 645 645 0 0 0 1611 966"/>
      <path id="arc-governance" d="M 460 966 A 506 506 0 0 1 1472 966"/>
      <path id="arc-protection" d="M 417 966 A 549 549 0 0 0 1515 966"/>
      <path id="arc-website" d="M 631.5 1087.8 A 356 356 0 0 1 904.2 615.4"/>
      <path id="arc-desktop" d="M 1027.8 615.4 A 356 356 0 0 1 1300.5 1087.8"/>
      <path id="arc-software" d="M 554 966 A 412 412 0 0 0 1378 966"/>
    </defs>

    <!-- layered rings -->
    <circle class="ring-threat" cx="966" cy="966" r="770"/>
    <circle class="ring-incident" cx="966" cy="966" r="666"/>
    <circle class="ring-trellaworks" cx="966" cy="966" r="595"/>
    <circle class="ring-divider" cx="966" cy="966" r="458"/>

    <!-- service cycle arrows -->
    <g class="service-cycle">
      <path class="service-arrow" d="M 581.1 1170.7 A 436 436 0 0 1 905.3 534.2 L 952.4 577.2 L 918.4 627.3 A 342 342 0 0 0 664.0 1126.6 L 605.3 1111.7 Z"/>
      <path class="service-arrow" d="M 981.2 530.3 A 436 436 0 0 1 1370.3 1129.3 L 1309.4 1148.6 L 1283.1 1094.1 A 342 342 0 0 0 977.9 624.2 L 1020.1 580.8 Z"/>
      <path class="service-arrow" d="M 1335.7 1197.0 A 436 436 0 0 1 622.4 1234.4 L 636.1 1172.1 L 696.5 1176.6 A 342 342 0 0 0 1256.0 1147.2 L 1272.5 1205.5 Z"/>
    </g>
    <circle class="core-disc" cx="966" cy="966" r="342"/>

    <!-- feedback loop -->
    <g class="feedback-loop">
      <path class="feedback-arrow" d="M 535.6 1214.5 A 497 497 0 0 1 508.5 771.8 L 528.8 780.4 L 520.8 687.8 L 436.7 741.4 L 456.9 749.9 A 553 553 0 0 0 487.1 1242.5 Z"/>
      <path class="feedback-arrow" d="M 1449.7 697.9 A 553 553 0 0 1 1475.0 1182.1 L 1495.3 1190.7 L 1420.7 1228.5 L 1403.2 1151.6 L 1423.5 1160.2 A 497 497 0 0 0 1400.7 725.1 Z"/>
      <text class="label-feedback" transform="translate(466 966) rotate(-90)" text-anchor="middle">FEEDBACK</text>
      <text class="label-feedback" transform="translate(1470 966) rotate(90)" text-anchor="middle">FEEDBACK</text>
    </g>

    <!-- ring labels -->
    <text class="label-outer"><textPath href="#arc-insurance" startOffset="50%" text-anchor="middle">TRELLAWORKS INSURANCE</textPath></text>
    <text class="label-outer"><textPath href="#arc-response" startOffset="50%" text-anchor="middle">INCIDENT RESPONSE</textPath></text>
    <text class="label-incident"><textPath href="#arc-incident" startOffset="50%" text-anchor="middle">INCIDENT</textPath></text>
    <text class="label-layer"><textPath href="#arc-governance" startOffset="50%" text-anchor="middle">TRELLAWORKS GOVERNANCE</textPath></text>
    <text class="label-layer"><textPath href="#arc-protection" startOffset="50%" text-anchor="middle">TRELLAWORKS PROTECTION</textPath></text>

    <!-- service labels -->
    <text class="label-service"><textPath href="#arc-website" startOffset="50%" text-anchor="middle">WEBSITE</textPath></text>
    <text class="label-service"><textPath href="#arc-desktop" startOffset="50%" text-anchor="middle">DESKTOP</textPath></text>
    <text class="label-service"><textPath href="#arc-software" startOffset="50%" text-anchor="middle">SOFTWARE</textPath></text>

    <!-- core title -->
    <text class="label-core" x="966" y="952" text-anchor="middle">QDR MSP</text>
    <text class="label-core" x="966" y="1050" text-anchor="middle">SERVICES</text>
  </svg>
</div>
</body>
</html>
```